Real Estate Business Card

Our Company, Brivora Real Estate needs a business card design. It will need a spot for our Name, Office Number, Cell number, email, website address. Brivorarealestate.example and Address. Please utilize our logo for the aesthetic feel of the card. We would like something that is noticeable but looks professional.

Please include our company tagline. "Where Real Estate and Real Easy Move You"

Industry/Entity Type

Business

Requirements
Should not have
• Black colored Font is OK. But other than that no black

```html
<!DOCTYPE html>
<html lang="en">
<head>
<meta charset="utf-8">
<title>Brivora Real Estate – Business Card</title>
<link rel="stylesheet" href="https://fonts.googleapis.com/css2?family=Noto+Sans:wght@400;600;700&display=swap">
<style>
  :root {
    --stage: #5fa3c4;
    --card: #ffffff;
    --brand-blue: #1f4fa0;
    --brand-orange: #ee7f24;
    --band-mid: #8a5f7a;
    --ink: #222222;
  }
  html, body {
    margin: 0;
    width: 1200px;
    height: 940px;
    overflow: hidden;
    background: var(--stage);
    font-family: "Noto Sans", sans-serif;
  }
  .business-card {
    position: absolute;
    left: 140px;
    top: 200px;
    width: 920px;
    height: 540px;
    background: var(--card);
    box-shadow: 0 10px 24px rgba(0, 0, 0, 0.35);
    overflow: hidden;
  }
  .top-edge {
    height: 14px;
    background: linear-gradient(90deg, var(--brand-blue), var(--band-mid) 45%, var(--brand-orange));
    border-bottom: 3px solid var(--brand-blue);
  }
  .brand-header {
    height: 150px;
    box-sizing: border-box;
    display: flex;
    align-items: center;
    padding-left: 44px;
    gap: 26px;
    border-bottom: 3px solid var(--brand-orange);
  }
  .brand-mark {
    flex: none;
    width: 120px;
    height: 100px;
    border-radius: 16px;
    background: var(--brand-orange);
  }
  .brand-text {
    display: flex;
    flex-direction: column;
    gap: 8px;
  }
  .brand-name {
    margin: 0;
    font-size: 70px;
    font-weight: 600;
    color: var(--brand-blue);
    letter-spacing: -1px;
    line-height: 1;
    white-space: nowrap;
  }
  .brand-tagline {
    margin: 0;
    font-size: 20px;
    font-weight: 400;
    color: var(--brand-orange);
    line-height: 1.1;
    white-space: nowrap;
  }
  .feature-band {
    height: 180px;
    background: linear-gradient(90deg, var(--brand-blue) 0%, #4a4f8c 35%, var(--band-mid) 55%, #c46f3e 78%, var(--brand-orange) 100%);
    border-bottom: 3px solid var(--brand-blue);
  }
  .contact-block {
    padding: 16px 26px 0 26px;
    text-align: right;
    color: var(--ink);
  }
  .contact-line {
    margin: 0 0 10px 0;
    display: flex;
    justify-content: flex-end;
    align-items: center;
    gap: 10px;
    white-space: nowrap;
  }
  .address-line { font-size: 29px; }
  .phone-line { font-size: 31px; }
  .web-line { font-size: 27px; justify-content: space-between; }
  .web-group { margin: 0; }
  .strong { font-weight: 700; }
  .divider { margin: 0 6px; }
  .contact-icon { flex: none; }
  .bottom-edge {
    position: absolute;
    left: 0;
    right: 0;
    bottom: 0;
    height: 8px;
    background: linear-gradient(90deg, var(--brand-orange), var(--band-mid) 50%, var(--brand-blue));
  }
</style>
</head>
<body>
  <div class="business-card">
    <div class="top-edge"></div>
    <header class="brand-header">
      <div class="brand-mark"></div>
      <div class="brand-text">
        <h1 class="brand-name">Brivora Real Estate</h1>
        <p class="brand-tagline">Where Real Estate and Real Easy Move You</p>
      </div>
    </header>
    <div class="feature-band" role="img" aria-label="Decorative band of faded house shapes blending from blue to orange"></div>
    <section class="contact-block">
      <p class="contact-line address-line">
        <svg class="contact-icon" width="26" height="30" viewBox="0 0 26 30" aria-hidden="true">
          <path d="M13 1C6.4 1 1.5 5.8 1.5 12c0 7.8 11.5 17 11.5 17s11.5-9.2 11.5-17C24.5 5.8 19.6 1 13 1z" fill="var(--brand-blue)"/>
          <circle cx="13" cy="12" r="4.2" fill="#fff"/>
        </svg>
        48 Larkmoor Lane, Ashwell, CT 06099
      </p>
      <p class="contact-line phone-line">
        <svg class="contact-icon" width="34" height="34" viewBox="0 0 24 24" aria-hidden="true">
          <path d="M6.6 10.8c1.4 2.8 3.8 5.1 6.6 6.6l2.2-2.2c.3-.3.7-.4 1-.2 1.1.4 2.3.6 3.6.6.6 0 1 .4 1 1V20c0 .6-.4 1-1 1C10.6 21 3 13.4 3 4c0-.6.4-1 1-1h3.5c.6 0 1 .4 1 1 0 1.3.2 2.5.6 3.6.1.3 0 .7-.2 1l-2.3 2.2z" fill="var(--brand-blue)"/>
        </svg>
        <span class="strong">(860)555-0142</span><span class="divider">|</span>cell: <span class="strong">(860)555-0187</span>
      </p>
      <p class="contact-line web-line">
        <span class="contact-line web-group">
          <svg class="contact-icon" width="40" height="30" viewBox="0 0 42 32" aria-hidden="true">
            <rect x="1" y="1" width="40" height="30" rx="3" fill="var(--brand-blue)"/>
            <path d="M3 4l18 14L39 4" fill="none" stroke="#fff" stroke-width="3"/>
          </svg>
          <span class="strong">Brivorarealestate.example</span>
        </span>
        <span><span class="divider">|</span>email@brivora.example</span>
      </p>
    </section>
    <div class="bottom-edge"></div>
  </div>
</body>
</html>
```